Business Card Design Project

Thornwick Property Management

Our Business is residential property management, we therefore need a card that displays a professional image, but is clear and concise, and easy to read
Updates

We are committed now guys and girls, loving what we are seeing so far! 

Target Market(s)

Landlords, Rental Property Owners

Industry/Entity Type

Residential

Requirements
Must have
• Dale Thornwick - Principal
Fiona Thornwick - Director (Property Management)

PO Box 817
Pellworth SA 5193

Dale: 0490 367 258
Fiona: 0490 723 519

www.thornwickpropertymanagement.com.au
admin@thornwickpropertymanagement.com.au

Nice to have
• I would like the card to be double sided, white background on the information side and then colour on the reverse, in blue or black and incorporating our logo

```html
<!DOCTYPE html>
<html lang="en">
<head>
<meta charset="utf-8">
<title>Thornwick Property Management – Business Card</title>
<link rel="stylesheet" href="https://fonts.googleapis.com/css2?family=Noto+Sans:wght@400;700&display=swap">
<style>
  :root {
    --backdrop: #e9e4da;
    --card: #151515;
    --card-edge: #0c0c0c;
    --text: #d9d9d9;
    --text-soft: #bdbdbd;
    --brand-white: #ffffff;
    --brand-blue: #1a8cf0;
    --rule: #6b6444;
    --ornament: #b09a4e;
  }
  html, body {
    margin: 0;
    width: 1200px;
    height: 900px;
    overflow: hidden;
    background: var(--backdrop);
    font-family: "Noto Sans", Verdana, sans-serif;
  }
  .canvas {
    position: relative;
    width: 1200px;
    height: 900px;
  }
  .card {
    position: absolute;
    top: 100px;
    width: 460px;
    height: 700px;
    background: var(--card);
    border: 1px solid var(--card-edge);
    border-radius: 14px;
    box-shadow: 0 10px 24px rgba(0,0,0,0.25);
    color: var(--text);
    text-align: center;
  }
  .card--info { left: 120px; }
  .card--brand { left: 620px; }

  .brand {
    position: absolute;
    left: 0;
    right: 0;
    display: flex;
    align-items: center;
    justify-content: center;
    gap: 14px;
  }
  .brand__mark {
    width: 34px;
    height: 34px;
    background: var(--brand-blue);
    flex: none;
  }
  .brand__name {
    margin: 0;
    font-weight: 700;
    font-size: 26px;
    line-height: 1.1;
    color: var(--brand-white);
    text-align: left;
  }
  .card--info .brand { top: 80px; }
  .card--brand .brand { top: 318px; }

  .divider {
    position: absolute;
    left: 110px;
    right: 110px;
    height: 20px;
  }
  .divider__line {
    position: absolute;
    top: 9px;
    height: 1px;
    width: 38%;
    background: var(--rule);
  }
  .divider__line--left { left: 0; }
  .divider__line--right { right: 0; }
  .divider__ornament {
    position: absolute;
    left: 50%;
    top: 2px;
    width: 40px;
    height: 16px;
    margin-left: -20px;
    border-radius: 8px;
    background: var(--ornament);
    opacity: 0.8;
  }
  .card--info .divider--top { top: 170px; }
  .card--info .divider--bottom { top: 500px; }
  .card--brand .divider--top { top: 250px; }
  .card--brand .divider--bottom { top: 430px; }

  .people {
    position: absolute;
    top: 268px;
    left: 0;
    right: 0;
    margin: 0;
  }
  .people__person {
    margin: 0 0 14px;
    font-size: 19px;
    letter-spacing: 0.3px;
  }
  .people__role-note {
    display: block;
    margin-top: 2px;
    font-size: 13px;
    color: var(--text-soft);
  }

  .contact {
    position: absolute;
    top: 548px;
    left: 0;
    right: 0;
    margin: 0;
    font-style: normal;
    font-size: 13px;
    line-height: 25px;
    color: var(--text-soft);
  }
</style>
</head>
<body>
<main class="canvas">

  <section class="card card--info" aria-label="Card front">
    <div class="brand">
      <span class="brand__mark"></span>
      <p class="brand__name">Thornwick<br>Property Management</p>
    </div>

    <div class="divider divider--top">
      <span class="divider__line divider__line--left"></span>
      <span class="divider__ornament" role="img" aria-label="Small gold scroll ornament"></span>
      <span class="divider__line divider__line--right"></span>
    </div>

    <div class="people">
      <p class="people__person">Dale Thornwick - Principal</p>
      <p class="people__person">Fiona Thornwick - Director
        <span class="people__role-note">(Property Management)</span>
      </p>
    </div>

    <div class="divider divider--bottom">
      <span class="divider__line divider__line--left"></span>
      <span class="divider__ornament" role="img" aria-label="Small gold scroll ornament"></span>
      <span class="divider__line divider__line--right"></span>
    </div>

    <address class="contact">
      PO Box 817, Pellworth SA 5193<br>
      Dale: 0490 367 258, Fiona: 0490 723 519<br>
      www.thornwickpropertymanagement.com.au<br>
      admin@thornwickpropertymanagement.com.au
    </address>
  </section>

  <section class="card card--brand" aria-label="Card back">
    <div class="divider divider--top">
      <span class="divider__line divider__line--left"></span>
      <span class="divider__ornament" role="img" aria-label="Small gold scroll ornament"></span>
      <span class="divider__line divider__line--right"></span>
    </div>

    <div class="brand">
      <span class="brand__mark"></span>
      <p class="brand__name">Thornwick<br>Property Management</p>
    </div>

    <div class="divider divider--bottom">
      <span class="divider__line divider__line--left"></span>
      <span class="divider__ornament" role="img" aria-label="Small gold scroll ornament"></span>
      <span class="divider__line divider__line--right"></span>
    </div>
  </section>

</main>
</body>
</html>
```